Require modern interface design for our website.

We are looking for a redesign of our website interface. The interface and the look and feel needs to be modern and seamless. Designer must be able to integrate with the backend PHP and Java. Please try utilise logo and colours where possible don't go too drastic. We utilise this site for learning and training purposes so please keep in line with that objective.

Target Market(s)

Education

Industry/Entity Type

Education

Number of Pages Required

5+ page

Font styles to use
Sans Serif

Requirements
Must have
• Innovative and modern look, logo to be incorporated.
Nice to have
• Good use of colours
Should not have
• Lack of creativity

```html
<!DOCTYPE html>
<html lang="en">
<head>
<meta charset="utf-8">
<title>Brightwick – Learning Platform</title>
<link rel="stylesheet" href="https://fonts.googleapis.com/css2?family=Open+Sans:ital,wght@0,400;0,600;0,700;1,600&display=swap">
<style>
:root{
  --blue:#1a9bf0;
  --blue-dark:#0f84d4;
  --ink:#333;
  --text:#666;
  --muted:#999;
  --line:#e6e6e6;
  --band:#f4f4f4;
  --white:#fff;
  --footer:#333;
  --footer-text:#aaa;
  --footer-base:#262626;
}
*{box-sizing:border-box;margin:0;padding:0}
html,body{width:1200px;height:3100px;overflow:hidden}
body{font-family:"Open Sans",Arial,sans-serif;color:var(--text);background:var(--white);font-size:13px;line-height:1.6}
.wrap{width:960px;margin:0 auto;position:relative}
a{color:inherit;text-decoration:none}

/* top bar */
.topbar{height:40px;border-bottom:1px solid var(--line);font-size:11px;color:var(--muted)}
.topbar .wrap{display:flex;justify-content:space-between;align-items:center;height:40px}
.topbar .social{display:flex;gap:8px}
.dot-icon{width:18px;height:18px;border-radius:50%;background:#d6d6d6;display:block}

/* nav */
.nav{height:72px;border-bottom:1px solid var(--line)}
.nav .wrap{display:flex;align-items:center;height:72px}
.brand{font-family:"Open Sans",Arial,sans-serif;font-size:26px;font-weight:700;color:var(--blue);line-height:1}
.menu{margin-left:auto;display:flex;align-items:center;gap:30px;font-size:11px;font-weight:600;color:var(--ink);text-transform:uppercase}
.menu .active{color:var(--blue);border-bottom:2px solid var(--blue);padding-bottom:4px}
.btn{display:inline-block;background:var(--blue);color:var(--white);font-size:12px;font-weight:600;padding:9px 26px;border-radius:2px}

/* hero */
.hero{height:408px;position:relative}
.hero-photo{position:absolute;inset:0;background:linear-gradient(100deg,#d9c1a8 0%,#9c7a5d 35%,#6f5443 60%,#4a3a33 100%)}
.hero-copy{position:absolute;left:630px;top:120px;width:520px;color:var(--white)}
.hero-copy h1{font-size:28px;font-weight:600;letter-spacing:2px;text-transform:uppercase;line-height:1.2;margin-bottom:12px;white-space:nowrap}
.hero-copy p{font-size:12px;line-height:1.6;margin-bottom:18px;opacity:.92;width:470px}

/* features */
.features{height:328px;border-bottom:1px solid var(--line)}
.features .wrap{display:flex;justify-content:space-between;padding-top:80px}
.feature{width:220px;text-align:center}
.feature .ring{width:70px;height:70px;border:2px solid #e4e4e4;border-radius:50%;margin:0 auto 24px;display:flex;align-items:center;justify-content:center}
.feature h3{font-size:14px;font-weight:600;color:var(--ink);margin-bottom:6px}
.feature p{font-size:11px;color:var(--muted);line-height:1.5}

/* section heads */
.section-title{text-align:center;font-size:28px;font-weight:400;color:var(--ink);line-height:1.2}
.section-sub{text-align:center;font-size:12px;color:var(--blue);margin-top:6px}
.section-lead{text-align:center;font-size:12px;color:var(--muted);margin-top:14px;line-height:1.6}

/* courses */
.courses{height:692px;background:var(--band);padding-top:80px}
.course-grid{display:flex;justify-content:space-between;margin-top:56px}
.course{width:308px;background:var(--white);border:1px solid var(--line)}
.course-photo{height:176px}
.course-body{padding:16px 18px 12px}
.course-body h3{font-size:15px;font-weight:600;color:var(--ink);padding-bottom:12px;border-bottom:1px solid var(--line);margin-bottom:12px}
.price{font-size:11px;color:var(--blue);font-weight:700}
.course-body p{font-size:11px;color:var(--muted);line-height:1.5;margin-top:4px}
.course-foot{display:flex;align-items:center;gap:16px;border-top:1px solid var(--line);padding:10px 18px;font-size:10px;color:var(--muted)}
.course-foot span{display:flex;align-items:center;gap:5px}
.course-foot .end{margin-left:auto}
.pager{display:flex;justify-content:center;gap:6px;margin-top:30px}
.pager i{width:12px;height:12px;border-radius:50%;border:1px solid #bbb;display:block}
.pager i.on{background:var(--blue);border-color:var(--blue)}

/* lecturers */
.lecturers{height:680px;padding-top:80px;border-bottom:1px solid var(--line)}
.lecturer-grid{display:grid;grid-template-columns:1fr 1fr;border:1px solid var(--line);margin-top:40px}
.lecturer{display:flex;gap:22px;padding:26px 28px;height:180px}
.lecturer:nth-child(odd){border-right:1px solid var(--line)}
.lecturer:nth-child(-n+2){border-bottom:1px solid var(--line)}
.avatar{width:110px;height:110px;border-radius:50%;flex:none;background:linear-gradient(135deg,#c9b6a6,#8a7466)}
.lecturer h3{font-size:15px;font-weight:600;color:var(--ink);margin:8px 0 10px}
.lecturer p{font-size:11px;color:var(--muted);line-height:1.5}
.link{display:inline-block;margin-top:10px;font-size:11px;color:var(--blue);font-weight:600}

/* students */
.students{height:500px;padding-top:60px}
.quote{width:740px;margin:34px auto 26px;text-align:center;font-size:19px;font-style:italic;font-weight:600;color:#555;line-height:1.5}
.student{text-align:center}
.student .avatar{width:100px;height:100px;margin:0 auto 14px}
.student h4{font-size:13px;font-weight:600;color:var(--ink)}
.student small{font-size:10px;color:var(--blue)}

/* footer */
.footer{height:320px;background:var(--footer);border-top:4px solid var(--blue);color:var(--footer-text);font-size:11px}
.footer .wrap{display:flex;justify-content:space-between;padding-top:40px}
.col{width:210px}
.col h5{color:var(--white);font-size:12px;font-weight:700;text-transform:uppercase;margin-bottom:18px}
.col p{line-height:1.7}
.col ul{list-style:none}
.col li{display:flex;align-items:center;gap:8px;margin-bottom:12px}
.news li{align-items:flex-start}
.thumb{width:36px;height:28px;flex:none;background:#555}
.news b{display:block;color:#ddd;font-weight:600}
.news em{font-style:normal;font-size:10px;color:#777}
.contact-icons{display:flex;gap:10px;margin-top:20px}
.contact-icons i{width:34px;height:34px;border-radius:50%;background:#444;display:flex;align-items:center;justify-content:center}
.base{height:60px;background:var(--footer-base);color:#888;font-size:10px}
.base .wrap{display:flex;justify-content:space-between;align-items:center;height:60px}
.base nav{display:flex;gap:26px;text-transform:uppercase;font-weight:600;color:#bbb}
</style>
</head>
<body>

<header class="topbar">
  <div class="wrap">
    <span>Phone: 0800 555 0142 &nbsp;|&nbsp; info@brightwick-learn.example</span>
    <div class="social"><i class="dot-icon"></i><i class="dot-icon"></i><i class="dot-icon"></i><i class="dot-icon"></i><i class="dot-icon"></i></div>
  </div>
</header>

<nav class="nav">
  <div class="wrap">
    <a class="brand" href="#">Brightwick</a>
    <div class="menu">
      <a class="active" href="#">Home</a>
      <a href="#">Courses</a>
      <a href="#">About</a>
      <a href="#">Blog</a>
      <a href="#">Contact</a>
      <svg width="14" height="14" viewBox="0 0 14 14"><circle cx="6" cy="6" r="4.5" fill="none" stroke="#333" stroke-width="1.6"/><line x1="9.3" y1="9.3" x2="13" y2="13" stroke="#333" stroke-width="1.6"/></svg>
      <a href="#">Log in</a>
      <a class="btn" href="#">Register</a>
    </div>
  </div>
</nav>

<section class="hero">
  <div class="hero-photo" role="img" aria-label="Smiling student holding books in a library"></div>
  <div class="hero-copy">
    <h1>Contrary to popular belief,</h1>
    <p>Lorem ipsum dolor sit amet, consectetur adipiscing elit, sed do eiusmod tempor incididunt ut labore et dolore magna aliqua. Ut enim ad minim veniam, quis nostrud exercitation ullamco laboris.</p>
    <a class="btn" href="#">Read More</a>
  </div>
</section>

<section class="features">
  <div class="wrap">
    <div class="feature">
      <div class="ring"><svg width="30" height="30" viewBox="0 0 24 24"><path d="M12 2l3 6.5 7 .8-5.2 4.8 1.4 7L12 17.6 5.8 21l1.4-7L2 9.3l7-.8z" fill="#1a9bf0"/></svg></div>
      <h3>Great Material</h3>
      <p>Lorem ipsum dolor sit amet consectetur adipiscing elit, sed do eiusmod tempor incididunt</p>
    </div>
    <div class="feature">
      <div class="ring"><svg width="32" height="32" viewBox="0 0 24 24" fill="none" stroke="#1a9bf0" stroke-width="2.2"><circle cx="9" cy="10" r="4"/><circle cx="17" cy="17" r="2.6"/><path d="M9 3v2M9 15v2M2 10h2M14 10h2M4 5l1.5 1.5M12.5 13.5L14 15M4 15l1.5-1.5M12.5 6.5L14 5"/></svg></div>
      <h3>High Quality</h3>
      <p>Lorem ipsum dolor sit amet consectetur adipiscing elit, sed do eiusmod tempor incididunt</p>
    </div>
    <div class="feature">
      <div class="ring"><svg width="30" height="30" viewBox="0 0 24 24"><path d="M12 21s-8-5.2-8-11a4.5 4.5 0 0 1 8-2.8A4.5 4.5 0 0 1 20 10c0 5.8-8 11-8 11z" fill="#1a9bf0"/></svg></div>
      <h3>Learning is Fun</h3>
      <p>Lorem ipsum dolor sit amet consectetur adipiscing elit, sed do eiusmod tempor incididunt</p>
    </div>
    <div class="feature">
      <div class="ring"><svg width="30" height="30" viewBox="0 0 24 24"><path d="M4 12.5l5 5L20 6.5" fill="none" stroke="#1a9bf0" stroke-width="3" stroke-linecap="round" stroke-linejoin="round"/></svg></div>
      <h3>It's simple</h3>
      <p>Lorem ipsum dolor sit amet consectetur adipiscing elit, sed do eiusmod tempor incididunt</p>
    </div>
  </div>
</section>

<section class="courses">
  <div class="wrap">
    <h2 class="section-title">Latest Courses</h2>
    <p class="section-sub">View all courses &rsaquo;</p>
    <div class="course-grid">
      <article class="course">
        <div class="course-photo" role="img" aria-label="Two people working together at a laptop" style="background:linear-gradient(135deg,#e8c46a,#8fb3cc)"></div>
        <div class="course-body">
          <h3>Internet Entrepreneurship</h3>
          <span class="price">$ 49</span>
          <p>Lorem ipsum dolor sit amet, consectetur adipiscing elit, sed do eiusmod tempor incididunt ut labore et dolore.</p>
        </div>
        <div class="course-foot"><span>&#9679; 12 Students</span><span>&#9679; Beginner</span><span class="end">&#9656;</span></div>
      </article>
      <article class="course">
        <div class="course-photo" role="img" aria-label="Video lesson title screen" style="background:linear-gradient(135deg,#d6e9f2,#4fa8c9)"></div>
        <div class="course-body">
          <h3>Online Video</h3>
          <span class="price">Free</span>
          <p>Lorem ipsum dolor sit amet, consectetur adipiscing elit, sed do eiusmod tempor incididunt ut labore et dolore.</p>
        </div>
        <div class="course-foot"><span>&#9679; 8 Students</span><span class="end">&#9656;</span></div>
      </article>
      <article class="course">
        <div class="course-photo" role="img" aria-label="Hands reviewing printed charts on a desk" style="background:linear-gradient(135deg,#f1f1f1,#a7b8c9)"></div>
        <div class="course-body">
          <h3>Course With Stream Video</h3>
          <span class="price">$ 25</span>
          <p>Lorem ipsum dolor sit amet, consectetur adipiscing elit, sed do eiusmod tempor incididunt ut labore et dolore.</p>
        </div>
        <div class="course-foot"><span>&#9679; 20 Students</span><span>&#9679; Intermediate</span><span class="end">&#9656;</span></div>
      </article>
    </div>
    <div class="pager"><i class="on"></i><i></i><i></i><i></i></div>
  </div>
</section>

<section class="lecturers">
  <div class="wrap">
    <h2 class="section-title">Lecturers</h2>
    <p class="section-lead">Our professional and experienced lecturers will make your course wonderful.<br>Our lecturers are practicing their field of expertise on daily basis.</p>
    <div class="lecturer-grid">
      <div class="lecturer">
        <div class="avatar" role="img" aria-label="Portrait of lecturer Dale Marsh"></div>
        <div><h3>Dale Marsh</h3><p>Lorem ipsum dolor sit amet, consectetur adipiscing elit, sed do eiusmod tempor incididunt ut labore et dolore magna.</p><a class="link" href="#">View Profile &#9656;</a></div>
      </div>
      <div class="lecturer">
        <div class="avatar" role="img" aria-label="Portrait of lecturer Kira Holt"></div>
        <div><h3>Kira Holt</h3><p>Lorem ipsum dolor sit amet, consectetur adipiscing elit, sed do eiusmod tempor incididunt ut labore et dolore magna.</p><a class="link" href="#">View Profile &#9656;</a></div>
      </div>
      <div class="lecturer">
        <div class="avatar" role="img" aria-label="Portrait of lecturer Nora Vance"></div>
        <div><h3>Nora Vance</h3><p>Lorem ipsum dolor sit amet, consectetur adipiscing elit, sed do eiusmod tempor incididunt ut labore et dolore magna.</p><a class="link" href="#">View Profile &#9656;</a></div>
      </div>
      <div class="lecturer">
        <div class="avatar" role="img" aria-label="Portrait of lecturer Elise Pardo"></div>
        <div><h3>Elise Pardo</h3><p>Lorem ipsum dolor sit amet, consectetur adipiscing elit, sed do eiusmod tempor incididunt ut labore et dolore magna.</p><a class="link" href="#">View Profile &#9656;</a></div>
      </div>
    </div>
  </div>
</section>

<section class="students">
  <div class="wrap">
    <h2 class="section-title">Our Students</h2>
    <p class="quote">"Lorem ipsum dolor sit amet, consectetur adipiscing elit, sed do eiusmod tempor incididunt ut labore et dolore magna aliqua."</p>
    <div class="student">
      <div class="avatar" role="img" aria-label="Portrait of student Tessa Lin"></div>
      <h4>Tessa Lin</h4>
      <small>Marketing Student</small>
    </div>
    <div class="pager"><i class="on"></i><i></i><i></i></div>
  </div>
</section>

<footer class="footer">
  <div class="wrap">
    <div class="col">
      <h5>About us</h5>
      <p>Lorem ipsum dolor sit amet, consectetur adipiscing elit, sed do eiusmod tempor incididunt ut labore et dolore magna aliqua enim.</p>
      <p style="margin-top:12px;color:#ddd">Learn more</p>
    </div>
    <div class="col">
      <h5>Links</h5>
      <ul>
        <li>&#9656; Theme Features</li>
        <li>&#9656; Typography</li>
        <li>&#9656; Isotopes</li>
        <li>&#9656; Register</li>
        <li>&#9656; Log In</li>
      </ul>
    </div>
    <div class="col news">
      <h5>News</h5>
      <ul>
        <li><span class="thumb" role="img" aria-label="News thumbnail"></span><span><b>Protected: Password</b><em>October 14, 2014</em></span></li>
        <li><span class="thumb" role="img" aria-label="News thumbnail"></span><span><b>Image Gallery</b><em>October 14, 2014</em></span></li>
        <li><span class="thumb" role="img" aria-label="News thumbnail"></span><span><b>Example Blog Post</b><em>October 14, 2014</em></span></li>
      </ul>
    </div>
    <div class="col">
      <h5>Get in touch!</h5>
      <p>Lorem ipsum dolor sit amet, consectetur adipiscing elit, sed do eiusmod tempor incididunt ut labore.</p>
      <div class="contact-icons">
        <i><svg width="16" height="12" viewBox="0 0 16 12"><rect x=".75" y=".75" width="14.5" height="10.5" fill="none" stroke="#bbb" stroke-width="1.5"/><path d="M1 1l7 6 7-6" fill="none" stroke="#bbb" stroke-width="1.5"/></svg></i>
        <i></i><i style="background:var(--blue)"></i><i></i>
      </div>
    </div>
  </div>
</footer>

<div class="base">
  <div class="wrap">
    <span>&copy; 2014 Brightwick Learning. All rights reserved.</span>
    <nav><a href="#">Home</a><a href="#">Courses</a><a href="#">Blog</a><a href="#">Contact</a></nav>
  </div>
</div>

</body>
</html>
```